Research Program Web Site

Goal:
-Create photoshop or HTML+CSS mockup of homepage for the Program for Knowledge Systems .
- Also create a child page which would be used to frame more detailed information - e.g. a list of publications, blog page, project activities, staff page.
Details:
The homepage is intended to convey:
- The mission of the program
- Link to overviews of research projects, preferably with brief teaser descriptions
- Display information on upcoming events, publications and tweets
- Show a connection to Varnell and the Varnell libraries
- Encourage viewers to follow/share content via social studio
Target audience:
- Research funders interested in an overview of the program, its major research areas, and research outputs (such as program publications and software, awards)
- Varnell community (faculty, library staff, and students) interested in current information (blogs/tweets), events, and possible collaboration opportunities
Hosting:
- The site will eventually be hosted on datahub.varnell.edu using a CMS (Quillet)
- There will be opportunity for further website implementation work if desired
Existing material:
- A text overview of the research program is included in the appendix attached to this document
- Much of the information on research projects is currently described here: http://drbkessler.blogvista.example/dr-kesslers-current-projects-and-research-aka-what-is-jonas-doing/ This content will be moved to the program site when completed.
Themes:
- Varnell color scheme is here, it is not required, but could be used for inspiration: http://web.varnell.edu/graphicidentity/colors/index.html
- Varnell libraries home page is here: http://libraries.varnell.edu/.
- The program page should borrow some design element from the library page if possible, and include the library and Varnell logos somewhere on the page - but not as the most prominent branding element.
- Overall look and feel should be professional and serious, but modern
Comparison sites:
For comparison here are several pages for similar sites that are done fairly well:
http://www.dornsurvey.org/
http://www.studio.varnell.edu/
http://www.qs.bellmore.edu/
- The dorn and studio sites have the cleanest design.
- Both dorn and qs are successful in conveying information about upcoming evevnts, publication and tweets
- Studio lab shows the right connection to larger organization
- Dorn site communicates better the mission of the organization
Updates
A number of you have noted that the program description attachment was missing. I have now uploaded it. Thanks much - Jonas
Thanks to those who have submitted designs so far. I have noticed that none of the designs thus far submitted include all of the elements requested in the design brief (task description). For clarification, I will emphasize these required elements:
- an area to describe the mission of the program
4. Branding/theming
Reason: Provide additional time for review of designs by colleagues on this end
Thanks,
Jonas
Target Market(s)
- Research funders interested in an overview of the program, its major research areas, and research outputs (such as program publications and software
Industry/Entity Type
Library
Requirements
Nice to have
- hemes:
Comparison sites:
http://www.studio.varnell.edu/

```html
<!DOCTYPE html>
<html lang="en">
<head>
<meta charset="utf-8">
<title>Jonas Kessler's Blog</title>
<link href="https://fonts.googleapis.com/css2?family=Questrial&family=Arimo:ital,wght@0,400;0,700;1,400&display=swap" rel="stylesheet">
<style>
:root{
  --red:#9e2a2b;
  --ink:#1a1a1a;
  --body:#333;
  --muted:#555;
  --rule:#d9d9d9;
  --black:#050505;
  --footer:#1f1f1f;
  --footer-text:#e6e6e6;
  --hero-light:#ececec;
  --hero-mid:#d6d6d6;
}
*{box-sizing:border-box;margin:0;padding:0}
html,body{width:887px;height:1200px;overflow:hidden;background:#fff}
body{position:relative;font-family:"Arimo",Arial,sans-serif;color:var(--body)}
.abs{position:absolute}
.display{font-family:"Questrial",sans-serif}

/* header */
.site-title{left:86px;top:16px;font-family:"Questrial",sans-serif;font-size:29px;color:var(--ink);letter-spacing:.3px}
.site-title .soft{color:#777}
.site-tagline{left:87px;top:46px;font-family:"Questrial",sans-serif;font-size:11.5px;color:var(--red)}
.social-top{left:686px;top:17px;display:flex;gap:5px}
.social-btn{width:18px;height:18px;border:1px solid #9a9a9a;border-radius:3px;background:linear-gradient(#fff,#e3e3e3)}
.search{left:639px;top:42px;width:130px;height:27px;border:1px solid #d5d5d5;border-radius:5px;font-size:9px;color:#888;padding:8px 0 0 12px;box-shadow:inset 0 1px 2px rgba(0,0,0,.08)}
.go{left:772px;top:42px;width:29px;height:27px;background:var(--black);border-radius:5px;color:#fff;font-family:"Questrial",sans-serif;font-size:12px;text-align:center;line-height:27px}

/* nav */
.nav{left:74px;top:77px;width:739px;height:31px;background:var(--black);border-radius:5px 5px 0 0;display:flex;align-items:center;padding-left:71px}
.nav a{font-family:"Questrial",sans-serif;font-size:12px;color:#fff;text-decoration:none;padding:0 13px;line-height:31px}
.nav a.current{background:#777;color:#111;width:50px;text-align:center;padding:0}
.nav a.wide{padding:0 14px 0 11px}

/* hero */
.hero{left:74px;top:108px;width:739px;height:270px;background:linear-gradient(90deg,var(--hero-light),#e2e2e2 45%,var(--hero-mid))}
.hero-shadow{left:74px;top:378px;width:739px;height:8px;background:radial-gradient(ellipse at top,rgba(0,0,0,.28),rgba(0,0,0,0) 70%)}
.hero-photo{left:480px;top:0;width:259px;height:270px;background:linear-gradient(180deg,#d3d3d3 0%,#b9a58a 55%,#a8824e 100%)}
.hero-card{left:48px;top:56px;width:372px;height:102px;border:1px solid #b5b5b5;background:rgba(240,240,240,.55);padding:17px 0 0 27px}
.hero-card h1{font-family:"Questrial",sans-serif;font-weight:400;font-size:15.5px;line-height:17px;color:var(--ink)}
.hero-card p{font-family:"Questrial",sans-serif;font-size:10px;line-height:11.5px;color:var(--red);margin-top:5px}
.dots{left:38px;top:247px;display:flex;gap:8px}
.dots span{width:7px;height:7px;border-radius:50%;background:#888}
.dots span.on{background:var(--red)}

/* welcome */
.welcome{left:0;top:400px;width:800px;text-align:center;font-family:"Questrial",sans-serif;font-size:24px;color:var(--red);letter-spacing:.4px}
.intro{left:90px;top:438px;width:710px;text-align:center;font-family:"Questrial",sans-serif;font-size:16px;line-height:18px;color:var(--ink)}
.divider{left:88px;width:712px;height:1px;background:linear-gradient(90deg,transparent,#ccc 20%,#ccc 80%,transparent)}
.vrule{width:1px;background:var(--rule)}

.col-title{font-family:"Questrial",sans-serif;font-size:16.5px;color:var(--red)}
.small{font-size:9.4px;line-height:13.4px;color:var(--body)}
.just{text-align:justify}
.more{width:55px;height:16px;background:var(--black);border-radius:5px;color:#fff;font-size:8px;text-align:center;line-height:16px}

.expert-photo{left:87px;top:540px;width:63px;height:83px;background:linear-gradient(160deg,#f2f2f2,#9a9a9a)}
.expert-lead{font-weight:700;color:var(--red);font-size:9.4px;line-height:13.4px}

.event{display:flex;gap:0;position:absolute;left:327px;width:220px}
.event .date{width:40px;position:relative;height:36px}
.event .flag{position:absolute;left:0;top:2px;width:11px;height:24px;background:var(--red);clip-path:polygon(0 0,100% 0,100% 100%,50% 80%,0 100%)}
.event .flag i{position:absolute;top:2px;left:1px;font-style:normal;color:#fff;font-size:6.5px}
.event .day{position:absolute;left:12px;top:-2px;font-family:"Questrial",sans-serif;font-size:19px;color:var(--ink)}
.event .mon{position:absolute;left:13px;top:19px;font-size:8.5px;color:var(--ink)}
.event p{width:180px;text-align:justify}

.list{list-style:none}
.list li{font-size:10px;color:var(--ink);display:flex;align-items:center}
.list svg{margin-right:9px}

.tweet{position:absolute;left:93px;width:200px;border-bottom:1px dotted #777;padding-bottom:7px}
.tweet .bird{position:absolute;left:0;top:4px;width:14px;height:10px;border-radius:50%;background:#333}
.tweet .bird.blue{background:#2f9fd6}
.tweet .txt{margin-left:24px;font-size:8.8px;line-height:13px;color:#666}
.tweet a{color:var(--red);text-decoration:none;display:block}
.tweet em{color:#444}

.post{position:absolute;left:338px;width:198px;border-bottom:1px dotted #777;padding-bottom:6px;display:flex}
.post .thumb{width:70px;height:51px;border:3px solid #fff;box-shadow:0 1px 3px rgba(0,0,0,.45);flex:none}
.post .body{margin-left:9px}
.post h3{font-weight:400;font-size:10px;color:var(--red);line-height:13px}
.post p{font-size:8.8px;line-height:13.4px;color:#666}

/* footer */
.footer{left:0;top:1038px;width:887px;height:162px;background:linear-gradient(#262626,#161616);color:var(--footer-text)}
.footer h4{font-family:"Questrial",sans-serif;font-weight:400;font-size:13px;color:#fff;position:absolute}
.footer .links{position:absolute;font-size:9.5px;line-height:17px;color:#fff}
.footer .contact{position:absolute;left:434px;top:56px;font-size:8.8px;line-height:17.5px;color:#fff}
.footer .social{position:absolute;left:281px;top:67px;display:flex;gap:5px}
.footer .social .social-btn{width:18px;height:18px;border-color:#aaa}
.map{position:absolute;left:599px;top:44px;width:202px;height:76px;border:2px solid #fff;background:linear-gradient(135deg,#ecebe6,#dcd8cc 60%,#e8e2b8)}
.copy{position:absolute;right:92px;top:143px;font-size:8px;color:#ccc}
</style>
</head>
<body>

<header>
  <div class="abs site-title">Jonas <span class="soft">Kessler's</span> Blog</div>
  <div class="abs site-tagline">Social and Information Science</div>
  <div class="abs social-top" aria-label="Social links">
    <div class="social-btn"></div><div class="social-btn"></div><div class="social-btn"></div><div class="social-btn"></div><div class="social-btn"></div>
  </div>
  <div class="abs search">Search</div>
  <div class="abs go">GO</div>
</header>

<nav class="abs nav">
  <a class="current" href="#">Home</a>
  <a href="#">Current Research</a>
  <a href="#">Planned Appearances (Where is Jonas?)</a>
  <a class="wide" href="#">About</a>
  <a href="#">JonasKessler.com</a>
</nav>

<section class="abs hero">
  <div class="abs hero-photo" role="img" aria-label="Photo of Dr. Kessler speaking into a microphone"></div>
  <div class="abs hero-card">
    <h1>Dr. Kessler's Current Projects and Research<br>(aka. What is Jonas Doing?)</h1>
    <p>(For conference &amp; such see forthcoming appearances.<br>And for stuff that is done see&nbsp; publications &amp; CV)</p>
  </div>
  <div class="abs dots"><span></span><span></span><span class="on"></span></div>
</section>
<div class="abs hero-shadow"></div>

<h2 class="abs welcome" style="left:0;width:800px;font-weight:400">Welcome to Our Website</h2>
<p class="abs intro">Lorem ipsum dolor sit amet, consectetur adipisicing elit, sed do eiusmod temporincididunt ut labore et dolore magna aliqua.</p>
<div class="abs divider" style="top:490px"></div>

<!-- row one -->
<div class="abs vrule" style="left:317px;top:516px;height:204px"></div>
<div class="abs vrule" style="left:562px;top:516px;height:204px"></div>

<h3 class="abs col-title" style="left:88px;top:508px;font-weight:400">Ask the Experts</h3>
<div class="abs expert-photo" role="img" aria-label="Portrait of a staff expert"></div>
<div class="abs small just" style="left:165px;top:542px;width:138px">
  <div class="expert-lead">The standard Lorem Ipsum passage,</div>
  <div style="margin-top:3px">Lorem ipsum dolor sit amet, consectetur adipisicing elit, sed do eiusmod tempor incididunt ut labore et laboris</div>
</div>
<p class="abs small just" style="left:89px;top:633px;width:214px">Lorem ipsum dolor sit amet, consectetur adipisicing elit, sed do eiusmod tempor incididunt ut labore et laboris</p>
<div class="abs more" style="left:247px;top:703px">Read more</div>

<h3 class="abs col-title" style="left:331px;top:508px;font-weight:400">News and Events</h3>
<div class="event" style="top:546px"><div class="date"><span class="flag"><i>13</i></span><span class="day">01</span><span class="mon">JAN</span></div><p class="small">Lorem ipsum dolor sit amet, consectetur adipisicing elit, sed do eiusmod tempor incididunt ut labore et laboris</p></div>
<div class="event" style="top:596px"><div class="date"><span class="flag"><i>13</i></span><span class="day">01</span><span class="mon">JAN</span></div><p class="small">Lorem ipsum dolor sit amet, consectetur adipisicing elit, sed do eiusmod tempor incididunt ut labore et laboris</p></div>
<div class="event" style="top:649px"><div class="date"><span class="flag"><i>13</i></span><span class="day">01</span><span class="mon">JAN</span></div><p class="small">Lorem ipsum dolor sit amet, consectetur adipisicing elit, sed do eiusmod tempor incididunt ut labore et laboris</p></div>
<div class="abs more" style="left:489px;top:703px">Read more</div>

<h3 class="abs col-title" style="left:597px;top:508px;font-weight:400">Library Services</h3>
<ul class="abs list" style="left:598px;top:541px">
  <li style="height:23.7px"><svg width="10" height="7" viewBox="0 0 10 7"><path d="M0 0L5 3.5L0 7ZM5 0L10 3.5L5 7Z" fill="#111"/></svg>Guides</li>
  <li style="height:23.7px"><svg width="10" height="7" viewBox="0 0 10 7"><path d="M0 0L5 3.5L0 7ZM5 0L10 3.5L5 7Z" fill="#111"/></svg>Borrow/request</li>
  <li style="height:23.7px"><svg width="10" height="7" viewBox="0 0 10 7"><path d="M0 0L5 3.5L0 7ZM5 0L10 3.5L5 7Z" fill="#111"/></svg>Help</li>
  <li style="height:23.7px"><svg width="10" height="7" viewBox="0 0 10 7"><path d="M0 0L5 3.5L0 7ZM5 0L10 3.5L5 7Z" fill="#111"/></svg>Tools</li>
  <li style="height:23.7px"><svg width="10" height="7" viewBox="0 0 10 7"><path d="M0 0L5 3.5L0 7ZM5 0L10 3.5L5 7Z" fill="#111"/></svg>Publishing</li>
  <li style="height:23.7px"><svg width="10" height="7" viewBox="0 0 10 7"><path d="M0 0L5 3.5L0 7ZM5 0L10 3.5L5 7Z" fill="#111"/></svg>Visit the library</li>
</ul>
<div class="abs more" style="left:719px;top:703px">Read more</div>

<div class="abs divider" style="top:741px"></div>

<!-- row two -->
<div class="abs vrule" style="left:317px;top:768px;height:256px"></div>
<div class="abs vrule" style="left:562px;top:768px;height:256px"></div>

<h3 class="abs col-title" style="left:88px;top:760px;font-weight:400">Latest Tweets</h3>
<div class="tweet" style="top:798px"><span class="bird"></span><div class="txt">Lorem ipsum dolor sit amet, consectetuer adipiscing elit, sed diam nonummy nibh<a href="#">http://lnk.example/k4q21</a><em>24 minutes ago</em></div></div>
<div class="tweet" style="top:862px"><span class="bird"></span><div class="txt">Lorem ipsum dolor sit amet, consectetuer adipiscing elit, sed diam nonummy nibh<a href="#">http://lnk.example/k4q21</a><em>24 minutes ago</em></div></div>
<div class="tweet" style="top:926px"><span class="bird blue"></span><div class="txt">Lorem ipsum dolor sit amet, consectetuer adipiscing elit, sed diam nonummy nibh<a href="#">http://lnk.example/k4q21</a><em>24 minutes ago</em></div></div>
<div class="abs more" style="left:247px;top:1007px">Read more</div>

<h3 class="abs col-title" style="left:331px;top:760px;font-weight:400">Recent Blog</h3>
<div class="post" style="top:791px"><div class="thumb" role="img" aria-label="Thumbnail photo of a red fruit" style="background:linear-gradient(135deg,#3a0a0a,#c8200f 55%,#6a0d08)"></div><div class="body"><h3>This is a sample Post 1</h3><p>Lorem ipsum dolor sit amet, consectetuer adipiscing elit, sed diam nonummy nibh...</p></div></div>
<div class="post" style="top:865px"><div class="thumb" role="img" aria-label="Thumbnail photo of a black and white rose" style="background:linear-gradient(135deg,#222,#8a8a8a 50%,#1a1a1a)"></div><div class="body"><h3>This is a sample Post 1</h3><p>Lorem ipsum dolor sit amet, consectetuer adipiscing elit, sed diam nonummy nibh...</p></div></div>
<div class="post" style="top:939px"><div class="thumb" role="img" aria-label="Thumbnail photo of a strawberry" style="background:radial-gradient(circle at 50% 55%,#c8261c 0,#a01810 28%,#e9e9e9 45%,#f7f7f7)"></div><div class="body"><h3>This is a sample Post 1</h3><p>Lorem ipsum dolor sit amet, consectetuer adipiscing elit, sed diam nonummy nibh...</p></div></div>
<div class="abs more" style="left:489px;top:1007px">Read more</div>

<h3 class="abs col-title" style="left:597px;top:760px;font-weight:400">Archives</h3>
<ul class="abs list" style="left:598px;top:789px">
  <li style="height:23.7px"><svg width="10" height="7" viewBox="0 0 10 7"><path d="M0 0L5 3.5L0 7ZM5 0L10 3.5L5 7Z" fill="#111"/></svg><span style="margin-left:4px">December 2012</span></li>
  <li style="height:23.7px"><svg width="10" height="7" viewBox="0 0 10 7"><path d="M0 0L5 3.5L0 7ZM5 0L10 3.5L5 7Z" fill="#111"/></svg><span style="margin-left:4px">November 2012</span></li>
  <li style="height:23.7px"><svg width="10" height="7" viewBox="0 0 10 7"><path d="M0 0L5 3.5L0 7ZM5 0L10 3.5L5 7Z" fill="#111"/></svg><span style="margin-left:4px">October 2012</span></li>
  <li style="height:23.7px"><svg width="10" height="7" viewBox="0 0 10 7"><path d="M0 0L5 3.5L0 7ZM5 0L10 3.5L5 7Z" fill="#111"/></svg><span style="margin-left:4px">September 2012</span></li>
  <li style="height:23.7px"><svg width="10" height="7" viewBox="0 0 10 7"><path d="M0 0L5 3.5L0 7ZM5 0L10 3.5L5 7Z" fill="#111"/></svg><span style="margin-left:4px">July 2012</span></li>
  <li style="height:23.7px"><svg width="10" height="7" viewBox="0 0 10 7"><path d="M0 0L5 3.5L0 7ZM5 0L10 3.5L5 7Z" fill="#111"/></svg><span style="margin-left:4px">June 2012</span></li>
  <li style="height:23.7px"><svg width="10" height="7" viewBox="0 0 10 7"><path d="M0 0L5 3.5L0 7ZM5 0L10 3.5L5 7Z" fill="#111"/></svg><span style="margin-left:4px">March 2012</span></li>
  <li style="height:23.7px"><svg width="10" height="7" viewBox="0 0 10 7"><path d="M0 0L5 3.5L0 7ZM5 0L10 3.5L5 7Z" fill="#111"/></svg><span style="margin-left:4px">January 2012</span></li>
  <li style="height:23.7px"><svg width="10" height="7" viewBox="0 0 10 7"><path d="M0 0L5 3.5L0 7ZM5 0L10 3.5L5 7Z" fill="#111"/></svg><span style="margin-left:4px">October 2011</span></li>
</ul>
<div class="abs more" style="left:719px;top:1007px">Read more</div>

<footer class="abs footer">
  <h4 style="left:85px;top:26px">Sitemap</h4>
  <div class="links" style="left:86px;top:47px">Home<br>About<br>Current Research<br>Planned Appearances</div>
  <div class="links" style="left:197px;top:47px">Blog<br>Contact</div>
  <h4 style="left:280px;top:36px">Follow Us On</h4>
  <div class="social"><div class="social-btn"></div><div class="social-btn"></div><div class="social-btn"></div><div class="social-btn"></div><div class="social-btn"></div></div>
  <h4 style="left:436px;top:36px">Contact Info</h4>
  <div class="contact">#12 Elmstead Road,Lorem ipsum,<br>P: +91 800112233&nbsp; T: (006) 60998877<br>E-mail: info@kesslerlab.example</div>
  <div class="map" role="img" aria-label="Street map showing the office location"></div>
  <div class="copy">© 2012.www.Varnell.com</div>
</footer>

</body>
</html>
```